Australian Wine export company Need a Wine label design

We need a wine label design for a new branded Australian wine based in South Australia called " KESTRELMOOR " .
We will use this brand name ' KESTRELMOOR' to marketing Australian Red wine and White wine into Chinese Market.
We would like to see the label designs that look classic and make consumers feel this is a superior quality Australian wine.
This label is to promote AUSTRALIAN WINE, need wine related and country related theme, need to give the consumer first impression that this wine is from AUSTRALIA.

Thanks

The following information are required to be presented on the wine label:

1) Brand Name: Kestrelmoor
2) Logo
3) Year of Vintage
4) Varietal
5) Place of production: South Australia
6) Fine Wine of Australia

Thanks.

Target Market(s)

Chinese market

Industry/Entity Type

Marketing

Requirements
Must have
• Need label design and renderings on the bottles.
Nice to have
• Label make consumers feel this is a superior quality Australian Wine.

```html
<!DOCTYPE html>
<html lang="en">
<head>
<meta charset="utf-8">
<title>Kestrelmoor Wine Labels</title>
<link rel="stylesheet" href="https://fonts.googleapis.com/css2?family=Josefin+Sans:wght@700&family=Montserrat:wght@400;600;700&family=Cinzel:wght@400;700&display=swap">
<style>
  :root {
    --canvas: #ffffff;
    --ink-brown: #4a2c20;
    --label-beige: #cbbfa8;
    --label-cream: #e9e3d7;
    --label-line: #f7f4ee;
    --map-light: #f4f1ea;
  }
  * { box-sizing: border-box; margin: 0; padding: 0; }
  html, body { width: 1200px; height: 927px; overflow: hidden; background: var(--canvas); }
  .canvas { position: relative; width: 1200px; height: 927px; }

  /* Neck label */
  .neck-label {
    position: absolute; left: 385px; top: 70px; width: 430px; height: 234px;
    background: var(--label-beige);
  }
  .neck-label__art {
    position: absolute; left: 120px; top: 26px; width: 190px; height: 120px;
    border-radius: 40px 60px 50% 50%;
    background: radial-gradient(circle at 55% 55%, #5a3a2c, var(--ink-brown));
  }
  .neck-label__caption {
    position: absolute; left: 0; right: 0; top: 172px; text-align: center;
    font-family: "Montserrat", sans-serif; font-weight: 600; font-size: 19px;
    color: var(--ink-brown);
  }

  /* Main label */
  .main-label { position: absolute; left: 445px; top: 368px; width: 310px; height: 428px; }
  .main-label__frame { position: absolute; inset: 0; }
  .main-label__map {
    position: absolute; left: 105px; top: 36px; width: 100px; height: 86px;
    border-radius: 30% 45% 40% 35%;
    background: linear-gradient(180deg, var(--map-light) 0 50%, var(--ink-brown) 50% 78%, var(--map-light) 78%);
  }
  .main-label__brand {
    position: absolute; left: 0; right: 0; top: 146px; text-align: center;
    font-family: "Josefin Sans", sans-serif; font-weight: 700; font-size: 31px;
    letter-spacing: 1px; color: var(--ink-brown);
  }
  .main-label__rule {
    position: absolute; left: 48px; right: 48px; height: 2px; background: var(--ink-brown);
  }
  .main-label__rule--upper { top: 188px; }
  .main-label__rule--lower { top: 222px; }
  .main-label__varietal {
    position: absolute; left: 0; right: 0; top: 197px; text-align: center;
    font-family: "Cinzel", serif; font-size: 15px; letter-spacing: 4px; color: var(--ink-brown);
  }
  .main-label__ornament {
    position: absolute; left: 48px; top: 236px; width: 214px; height: 40px;
    border-radius: 20px;
    background: linear-gradient(90deg, transparent, var(--ink-brown) 20%, var(--ink-brown) 80%, transparent);
    opacity: 0.85;
  }
  .main-label__details {
    position: absolute; left: 30px; right: 30px; top: 306px;
    display: flex; justify-content: space-between; align-items: flex-end;
    font-family: "Montserrat", sans-serif; color: var(--ink-brown);
  }
  .details__abv, .details__volume { font-size: 11px; font-weight: 600; line-height: 1.1; }
  .details__place { text-align: center; }
  .details__place-label { font-size: 10px; font-weight: 700; }
  .details__place-name { font-size: 17px; font-weight: 600; line-height: 1.1; }
  .main-label__vintage {
    position: absolute; left: 105px; top: 350px; width: 100px; text-align: center;
    font-family: "Montserrat", sans-serif; color: var(--ink-brown);
  }
  .vintage__label { font-size: 9px; font-weight: 700; letter-spacing: 2px; }
  .vintage__ribbon { position: relative; height: 24px; margin-top: 2px; }
  .vintage__ribbon svg { position: absolute; inset: 0; }
  .vintage__year {
    position: relative; font-size: 17px; font-weight: 600; letter-spacing: 2px; line-height: 24px;
  }
</style>
</head>
<body>
<main class="canvas">

  <section class="neck-label">
    <div class="neck-label__art" role="img" aria-label="Illustration of a grape bunch with leaves"></div>
    <p class="neck-label__caption">Australia Wine</p>
  </section>

  <section class="main-label">
    <svg class="main-label__frame" viewBox="0 0 310 428" width="310" height="428" aria-hidden="true">
      <path fill="var(--label-cream)" d="M10 70 Q28 70 28 50 Q90 50 120 22 Q155 -2 190 22 Q220 50 282 50 Q282 70 300 70 L300 358 Q282 358 282 378 Q220 378 190 406 Q155 430 120 406 Q90 378 28 378 Q28 358 10 358 Z"/>
      <path fill="var(--label-beige)" transform="translate(155 214) scale(0.94) translate(-155 -214)" d="M10 70 Q28 70 28 50 Q90 50 120 22 Q155 -2 190 22 Q220 50 282 50 Q282 70 300 70 L300 358 Q282 358 282 378 Q220 378 190 406 Q155 430 120 406 Q90 378 28 378 Q28 358 10 358 Z"/>
      <path fill="none" stroke="var(--label-line)" stroke-width="1.5" transform="translate(155 214) scale(0.89) translate(-155 -214)" d="M10 70 Q28 70 28 50 Q90 50 120 22 Q155 -2 190 22 Q220 50 282 50 Q282 70 300 70 L300 358 Q282 358 282 378 Q220 378 190 406 Q155 430 120 406 Q90 378 28 378 Q28 358 10 358 Z"/>
    </svg>

    <div class="main-label__map" role="img" aria-label="Map of Australia with South Australia highlighted"></div>
    <h1 class="main-label__brand">KESTRELMOOR</h1>
    <div class="main-label__rule main-label__rule--upper"></div>
    <p class="main-label__varietal">VARIETAL</p>
    <div class="main-label__rule main-label__rule--lower"></div>
    <div class="main-label__ornament" role="img" aria-label="Decorative flourish with a wine glass"></div>

    <div class="main-label__details">
      <p class="details__abv">14%<br>Alc/Vol</p>
      <div class="details__place">
        <p class="details__place-label">Place of Production</p>
        <p class="details__place-name">South Australia</p>
      </div>
      <p class="details__volume">750ml</p>
    </div>

    <div class="main-label__vintage">
      <p class="vintage__label">VINTAGE</p>
      <div class="vintage__ribbon">
        <svg viewBox="0 0 100 24" width="100" height="24" aria-hidden="true">
          <path d="M2 4 L14 4 L14 20 L2 20 L7 12 Z" fill="var(--ink-brown)"/>
          <path d="M98 4 L86 4 L86 20 L98 20 L93 12 Z" fill="var(--ink-brown)"/>
          <rect x="16" y="2" width="68" height="20" fill="var(--label-cream)" stroke="var(--ink-brown)" stroke-width="1.5"/>
        </svg>
        <p class="vintage__year">2000</p>
      </div>
    </div>
  </section>

</main>
</body>
</html>
```